Need a business card for our overland brand!

We had the logo made and we need a great design for our business card. Use the logo provide or tweak it however you see fit.

Contact Information for Business Card

Name, Title, Telephone, email, website

```html
<!DOCTYPE html>
<html lang="en">
<head>
<meta charset="utf-8">
<title>Ridgeway Expeditions – Business Card</title>
<link rel="stylesheet" href="https://fonts.googleapis.com/css2?family=Montserrat:wght@400;700;800&display=swap">
<style>
  :root {
    --navy: #233a55;
    --navy-deep: #1f344d;
    --navy-faint: #2c4866;
    --ice: #2aa3cf;
    --paper: #ffffff;
    --ink: #1e2f45;
    --stage: #e9ebee;
  }
  * { box-sizing: border-box; margin: 0; padding: 0; }
  html, body { width: 1200px; height: 931px; overflow: hidden; }
  body {
    background: var(--stage);
    font-family: "Montserrat", sans-serif;
    color: var(--ink);
    position: relative;
  }
  .card {
    position: absolute;
    width: 700px;
    height: 400px;
    border-radius: 22px;
    overflow: hidden;
    box-shadow: 0 10px 28px rgba(20, 30, 45, 0.22);
  }
  /* Back side */
  .card-back {
    left: 250px;
    top: 45px;
    background: var(--navy);
    display: flex;
    align-items: center;
    justify-content: center;
  }
  .card-back .brand-mark {
    font-weight: 800;
    font-size: 44px;
    line-height: 1.05;
    text-transform: uppercase;
    text-align: center;
    color: var(--navy-faint);
    letter-spacing: 1px;
  }
  /* Front side */
  .card-front {
    left: 250px;
    top: 485px;
    background: var(--paper);
  }
  .card-front .base-band {
    position: absolute;
    left: 0; right: 0; bottom: 0;
    height: 16px;
    background: var(--navy);
  }
  .card-front .brand-mark {
    position: absolute;
    right: 60px;
    top: 50px;
    width: 250px;
    font-weight: 800;
    font-size: 34px;
    line-height: 1.05;
    text-transform: uppercase;
    text-align: center;
    color: var(--navy);
  }
  .divider {
    position: absolute;
    left: 48px;
    right: 36px;
    top: 222px;
    height: 2px;
    background: var(--navy);
  }
  .identity {
    position: absolute;
    left: 48px;
    top: 166px;
  }
  .identity .name {
    font-weight: 700;
    font-size: 30px;
    color: var(--navy);
    line-height: 1;
  }
  .identity .title {
    font-weight: 400;
    font-size: 16px;
    margin-top: 4px;
  }
  .contacts {
    position: absolute;
    left: 60px;
    top: 244px;
    list-style: none;
  }
  .contacts li {
    display: flex;
    align-items: center;
    gap: 14px;
    font-size: 17px;
    height: 34px;
  }
  .contacts svg { width: 20px; height: 20px; flex: none; }
  .address {
    position: absolute;
    right: 44px;
    top: 244px;
    font-size: 15px;
    line-height: 1.4;
    text-align: right;
  }
</style>
</head>
<body>

<section class="card card-back" aria-label="Card back">
  <div class="brand-mark">Ridgeway<br>Expeditions</div>
</section>

<section class="card card-front" aria-label="Card front">
  <div class="brand-mark">Ridgeway<br>Expeditions</div>

  <div class="identity">
    <p class="name">Daniel Hale</p>
    <p class="title">Managing Director</p>
  </div>

  <div class="divider"></div>

  <ul class="contacts">
    <li>
      <svg viewBox="0 0 20 20" aria-hidden="true"><path fill="#2aa3cf" d="M3 7c0-2 3-4 7-4s7 2 7 4v1h-4V6.5c-1.9-.6-4.1-.6-6 0V8H3zM5 10l2-2h6l2 2v6H5z"/><circle cx="10" cy="12.5" r="2" fill="#fff"/></svg>
      555-014-2276
    </li>
    <li>
      <svg viewBox="0 0 20 20" aria-hidden="true"><rect x="2" y="5" width="16" height="11" rx="1" fill="#2aa3cf"/><path d="M2.5 5.5 10 11l7.5-5.5" fill="none" stroke="#fff" stroke-width="1.3"/></svg>
      info@ridgewayexpeditions.com
    </li>
    <li>
      <svg viewBox="0 0 20 20" aria-hidden="true"><circle cx="10" cy="10" r="8" fill="#2aa3cf"/><path d="M2 10h16M10 2c3 3 3 13 0 16M10 2c-3 3-3 13 0 16" fill="none" stroke="#fff" stroke-width="1.1"/></svg>
      www.ridgewayexpeditions.com
    </li>
  </ul>

  <p class="address">418 Cedar Hollow Rd, #112<br>Lakemont, OH 43990</p>

  <div class="base-band"></div>
</section>

</body>
</html>
```